Graphic Design Project - Top Ten Tips for Surviving a Tax Investigation Graphic/Infographic

This is a challenging one so I need someone really good to convert this into a useful graphic.

I have some content around top tips for Surviving a Tax Investigation. Not sure if this can be represented in an "infographic" as its not data - centric (more of a top ten list) but i would like some kind of infographic based image to share around my social networks.

The content is as follows - obviously the text will need to be reduced significantly without losing the message and it must allow a link and be branded as Pendrake Tax (www.pendraketax.co.uk)

_________________________________________________

Surviving a Tax Investigation

So what are the key things to do (or not to do).

1. Don’t Panic

For many here will be an initial knee jerk reaction such as fear,denial and anger or a desire to have a chat with the Inspector to show you are a good person and willing to help or to assure BQTF there is nothing wrong.
This is a time for cool heads, planning and contemplation as to what could be the problems and taking stock of the situation. Do not do anything rash and:

2. Take Expert advice

Your fist discussion may be with your accountant. Some are good at tax investigation work, many are not specialists. Engaging a specialist can make all the difference in time taken to deal with the issues and the eventual outcome. You must have an open and honest conversation about what may or may not have gone on and sometimes this is difficult with existing advisors. An expert in the field of tax investigations understands the legal frame work in which BQTF operates and the subtleties of tax investigations which can be used to your advantage. After all you would not ask a GP to conduct specialised surgery.

3. Don’t Lie

Tell your advisor the truth, if you have chosen well then they will be able to manage the situation properly. If there is something wrong then it is best this is disclosed to BQTF at the earliest given opportunity.

4. BQTF already knows quite a lot

BQTF rarely go on ‘fishing expeditions’. Before any tax investigation they review your tax returns and research their ‘data warehouse’ for background information on property and other assets, interest bearing bank accounts and now they have access to various information from Q5 countries including overseas property. Often they will have sufficient evidence to suspect that there are problems with your tax affairs. If you do not tell them and they have to tell you then the costs of sorting the matter out goes up significantly.

5.Think critically

Think about what has gone wrong (if it has) and how it has happened. Before sending anything to BQTF or make sure you it has been looked at and consider if anything needs explanation.
Make sure if any bank statements are sent to BQTF that any none business deposits are explained.

6.Prepare for meetings

If you do attend a meeting make sure you are prepared. Anticipate any questions (this is where an experience advisor really helps) and think about your answers. Never attend without an advisor and ensure you take notes of what was said. Meetings are not just about finding more about the business, they are designed to catch you out.

7. Question what BQTF are asking for

BQTF often ask for things that they are not entitled to or send out onerous requests. Ask them why they need the information and think about what it has to do with your tax affairs. If the answer is it is nothing to do with your tax return then it is unlikely that it should be provided.

8. Deadline Management

BQTF Officers are under tremendous internal pressure to keep Investigations flowing. They will often suggest deadlines for the provision of information and responses. Often these are unreasonable. If you think they are entitled to the information then think about how long it will take you to do as they ask. Then tell them how long you think it will take to do. Remember where there are delays BQTF have unavoidable delays due to pressure of work, you are not cooperating!

9.Make Payments on Account

If you do owe tax then (if you have the funds) you should make payments on account to BQTF.
This demonstrates cooperation with BQTF and stops the clock of further interest accruing from the date the payment is made on the amount of the payment.

10.Find Solutions

At certain points in a tax investigation there will be questions to which no one knows the answer or technical ‘grey’ areas where the answer is unclear. Make pragmatic suggestions to BQTF as to how these could be resolved

11.Mitigate Penalties/Name and Shame

Penalties are based on perceived behaviour so make sure you understand how these work and read BQTF’s own guidance on this. Ensure that all answers to questions support the behaviour that you think has happened and that the penalty mitigation factors have all been covered. The difference between disclosing problems and helping sort them out, or denying them can reduce penalties by a massive margin. Behaviour during the enquiry can also have an influence on whether you appear on the quarterly name and shame list of “tax cheats” or not. Make sure you are not.

12.Don’t Do It Again!

BQTF do not look favourably on second time offenders and at best they will charge you a high penalty and these are always looked at more seriously for prosecution. Tax investigations are such a traumatic experience that most people never want to experience them again.

_________________________________

A draft will need to be submitted show a wireframe and look and feel for review towards the beginning of the project to allow for amends. Estimated 2-3 amends total throughout the life of the project.

Remember this is targeted to the UK market so spelling and grammar need to reflect this

I would like applicants to send me examples of their work. This needs to be highly professional and supplied as illustrator or photoshop files as well as JPG/PNG

Theme = highly professional, serious, on brand, emulating expertise, confident yet friendly- these people are on your side.

The files attached give you an idea of the theme of the brand

finance professionals, customers

Legal

• icons/graphics - should not be all text, needs to be as creative as possible given the content is heavy text

```html
<!DOCTYPE html>
<html lang="en-GB">
<head>
<meta charset="utf-8">
<title>Surviving a Tax Investigation – Pendrake Tax</title>
<link rel="stylesheet" href="https://fonts.googleapis.com/css2?family=Open+Sans:wght@700&family=PT+Sans+Narrow:wght@400;700&family=Montserrat:wght@700&family=Roboto:wght@300;400&display=swap">
<style>
  :root {
    --sky-top: #2d5fa8;
    --sky-mid: #6f9bd0;
    --sky-low: #c9dcec;
    --grass: #5f8f2a;
    --grass-dark: #3f6a18;
    --ink: #2b2b2b;
    --navy: #1f4e9c;
    --steel: #3f6f96;
    --pale-blue: #d6e8f7;
    --soft-blue: #6f93b0;
    --white: #ffffff;
    --panel-dark: #333333;
    --panel-light: rgba(255, 255, 255, 0.82);
  }
  * { margin: 0; padding: 0; box-sizing: border-box; }
  html, body { width: 927px; height: 1200px; overflow: hidden; background: #ffffff; }
  .poster {
    position: relative;
    width: 927px;
    height: 1200px;
    overflow: hidden;
    font-family: "PT Sans Narrow", "Arial Narrow", sans-serif;
  }
  .scene {
    position: absolute;
    inset: 0;
    background:
      linear-gradient(180deg, transparent 0 76%, #a9c46e 78.5%, var(--grass) 84%, var(--grass-dark) 100%),
      linear-gradient(180deg, var(--sky-top) 0%, var(--sky-mid) 30%, var(--sky-low) 62%, #e6eef3 78%);
  }
  .scene-figure {
    position: absolute;
    left: 310px;
    top: 650px;
    width: 560px;
    height: 340px;
    background: radial-gradient(ellipse at 50% 60%, rgba(60, 62, 70, 0.35) 0 22%, rgba(230, 235, 240, 0.25) 45%, transparent 70%);
  }
  .logo-box {
    position: absolute;
    left: 0; top: 37px;
    width: 399px; height: 153px;
    background: var(--white);
    display: flex;
    align-items: center;
    gap: 14px;
    padding-left: 48px;
  }
  .logo-mark {
    width: 26px; height: 26px;
    background: var(--navy);
  }
  .logo-name {
    font-family: "Open Sans", Arial, sans-serif;
    font-weight: 700;
    font-size: 38px;
    line-height: 1;
    color: var(--navy);
    white-space: nowrap;
  }
  .call {
    position: absolute;
    right: 37px; top: 70px;
    text-align: right;
    color: var(--white);
  }
  .call-label { font-size: 37px; line-height: 1.1; }
  .call-number { font-family: "Open Sans", Arial, sans-serif; font-weight: 700; font-size: 40px; line-height: 1.2; }
  .title {
    position: absolute;
    left: 0; right: 0; top: 226px;
    text-align: center;
    font-family: "Open Sans", Arial, sans-serif;
    font-weight: 700;
    font-size: 56px;
    color: var(--white);
    padding-left: 10px;
  }
  .tip { position: absolute; line-height: 1; white-space: nowrap; }
  .tip-panic { left: 109px; top: 336px; font-size: 46px; font-weight: 700; color: var(--ink); }
  .tip-expert { left: 320px; top: 370px; font-size: 47px; font-weight: 700; color: var(--white); }
  .tip-lie { left: 665px; top: 412px; font-size: 46px; font-weight: 700; color: var(--pale-blue); }
  .tip-knows { left: 37px; top: 472px; font-size: 59px; color: var(--ink); }
  .tip-critical { left: 614px; top: 536px; font-size: 56px; color: var(--white); }
  .tip-meetings { left: 67px; top: 563px; font-size: 58px; color: var(--navy); }
  .tip-question { left: 488px; top: 612px; font-size: 34px; color: var(--ink); }
  .tip-deadline { left: 63px; top: 668px; font-family: "Montserrat", Arial, sans-serif; font-weight: 700; font-size: 35.5px; color: var(--steel); }
  .tip-payments { left: 43px; top: 798px; font-size: 38px; color: var(--navy); }
  .tip-penalties { left: 26px; top: 869px; font-size: 26px; color: var(--ink); }
  .tip-again { left: 714px; top: 856px; font-size: 26px; color: var(--soft-blue); }
  .info-panel {
    position: absolute;
    left: 0; top: 989px;
    width: 652px; height: 156px;
    background: var(--panel-light);
    padding: 14px 0 0 18px;
    font-size: 19.5px;
    line-height: 27.5px;
    color: var(--ink);
    white-space: nowrap;
  }
  .help-panel {
    position: absolute;
    left: 652px; top: 989px;
    width: 275px; height: 156px;
    background: var(--panel-dark);
    color: var(--white);
    padding: 20px 0 0 20px;
    font-family: "Roboto", Arial, sans-serif;
  }
  .help-slogan { font-weight: 300; font-size: 29px; line-height: 35px; letter-spacing: 1.5px; }
  .help-note { font-size: 10px; margin-top: 18px; }
  .help-phone { font-size: 20px; margin-top: 3px; }
  .web {
    position: absolute;
    right: 18px; top: 1157px;
    font-family: "Open Sans", Arial, sans-serif;
    font-weight: 700;
    font-size: 24px;
    color: var(--white);
  }
</style>
</head>
<body>
<main class="poster">
  <div class="scene" role="img" aria-label="Photograph of a bright blue sky with clouds over a green grass field"></div>
  <div class="scene-figure" role="img" aria-label="Photograph of a businessman seen from behind, sitting in an office chair on the grass with arms stretched out"></div>

  <div class="logo-box">
    <span class="logo-mark"></span>
    <span class="logo-name">Pendrake Tax</span>
  </div>

  <div class="call">
    <div class="call-label">Call Us Now</div>
    <div class="call-number">0800 512 6470</div>
  </div>

  <h1 class="title">Surviving a Tax Investigation</h1>

  <p class="tip tip-panic">Don’t Panic</p>
  <p class="tip tip-expert">Take Expert advice</p>
  <p class="tip tip-lie">Don’t Lie</p>
  <p class="tip tip-knows">BQTF already knows quite a lot</p>
  <p class="tip tip-critical">Think critically</p>
  <p class="tip tip-meetings">Prepare for meetings</p>
  <p class="tip tip-question">Question what BQTF are asking for</p>
  <p class="tip tip-deadline">Deadline Management</p>
  <p class="tip tip-payments">Make Payments on Account</p>
  <p class="tip tip-penalties">Mitigate Penalties/Name and Shame</p>
  <p class="tip tip-again">Don’t Do It Again!</p>

  <div class="info-panel">
    For a private discussion about how we can resolve your tax investigation and potentially<br>
    save you money contact us at any time using the detail below. Our initial discussion will be<br>
    undertaken without charge. Although our main base is in the North of England we have<br>
    clients all over the country and offices available in Leeds, London and Birmingham.
  </div>

  <div class="help-panel">
    <div class="help-slogan">Here to help,<br>not to judge.</div>
    <div class="help-note">For helpful, no obligation and confidential advice call</div>
    <div class="help-phone">0800 512 6470</div>
  </div>

  <div class="web">www.pendraketax.co.uk</div>
</main>
</body>
</html>
```